New Business Card Design For Re-Branded Company (New Logo)

We recently switched our DBA and had a new logo designed. We now need new business cards made around our new logo. We would like to stick with the color scheme in our logo: White, Orange, and Blue. We want to see original bold designs that reflect our position in the solar energy sector but we prefer simple over complicated.

We are curious about vertical designs so if you can translate your design onto a vertical layout we would be open to look at it. We especially like a few designs we have seen on here that are vertical with a black or very dark gray background. They have our logo on one side and then the normal vertical business card on the other side.

I have included a screenshot of one of the samples we like, labeled sample.jpg and a file we were given as an example of our logo on a dark background.

At the same time we are satisfied to stay with what we have always had in a horizontal format. If it's not a lot of extra work for you, designs that are submitted in both horizontal and vertical formats will be greatly appreciated.

Please submit your original, bold, clean designs for consideration. Contact us with any questions or comments that may arise.

Thank you and Good Luck,

KP

```html
<!DOCTYPE html>
<html lang="en">
<head>
<meta charset="utf-8">
<title>Kestrel Power – Business Card</title>
<link href="https://fonts.googleapis.com/css2?family=Montserrat:wght@600&family=Source+Sans+3:wght@400;600&display=swap" rel="stylesheet">
<style>
  :root {
    --stage-top: #2b2b2b;
    --stage-bottom: #000000;
    --card-light: #e6e7e8;
    --brand-blue: #1e73be;
    --brand-orange: #f07a22;
    --ink: #3a3a3a;
    --white: #ffffff;
  }
  html, body {
    margin: 0;
    padding: 0;
    overflow: hidden;
  }
  .stage {
    position: relative;
    width: 1200px;
    height: 900px;
    background: linear-gradient(180deg, var(--stage-top) 0%, #141414 60%, var(--stage-bottom) 100%);
    overflow: hidden;
  }
  .card {
    position: absolute;
    top: 184px;
    height: 491px;
    box-sizing: border-box;
  }
  .card-front {
    left: 298px;
    width: 302px;
    background: var(--card-light);
    border-radius: 0 12px 12px 0;
    text-align: center;
    font-family: "Source Sans 3", "Myriad Pro", sans-serif;
    color: var(--ink);
  }
  .card-back {
    left: 645px;
    width: 305px;
    background: var(--brand-blue);
    border-radius: 12px;
  }
  .brand-dot {
    position: absolute;
    left: 133px;
    top: 52px;
    width: 36px;
    height: 36px;
    border-radius: 50%;
    background: var(--brand-orange);
  }
  .brand-name {
    position: absolute;
    left: 0;
    right: 0;
    margin: 0;
    font-family: "Montserrat", "Helvetica Neue", sans-serif;
    font-weight: 600;
    white-space: nowrap;
    text-align: center;
  }
  .card-front .brand-name {
    top: 120px;
    font-size: 28px;
    color: var(--brand-blue);
    letter-spacing: -0.3px;
  }
  .card-back .brand-name {
    top: 260px;
    font-size: 30px;
    color: var(--white);
    letter-spacing: -0.5px;
  }
  .person {
    position: absolute;
    top: 266px;
    left: 0;
    right: 0;
  }
  .person-name {
    margin: 0;
    font-size: 20px;
    font-weight: 600;
    color: var(--brand-blue);
    line-height: 1.2;
  }
  .person-role {
    margin: 2px 0 0;
    font-size: 15px;
    line-height: 1.2;
  }
  .contact {
    position: absolute;
    top: 342px;
    left: 0;
    right: 0;
    margin: 0;
    padding: 0;
    list-style: none;
    font-size: 15px;
    line-height: 20px;
  }
  .contact li {
    display: flex;
    justify-content: center;
    align-items: center;
    gap: 9px;
  }
  .contact svg {
    width: 10px;
    height: 10px;
    fill: var(--brand-blue);
  }
  .address {
    position: absolute;
    top: 419px;
    left: 0;
    right: 0;
    margin: 0;
    font-style: normal;
    font-size: 15px;
    line-height: 17px;
  }
</style>
</head>
<body>
<main class="stage">
  <section class="card card-front" aria-label="Business card front">
    <span class="brand-dot" aria-hidden="true"></span>
    <p class="brand-name">KESTREL POWER</p>
    <div class="person">
      <p class="person-name">DANIEL REYES</p>
      <p class="person-role">Managing Direcator</p>
    </div>
    <ul class="contact">
      <li>
        <svg viewBox="0 0 10 10" aria-hidden="true"><path d="M1 3.2C1 2 2.4 1.3 5 1.3S9 2 9 3.2L7.4 4 6.6 3H3.4L2.6 4zM2.5 5.2 4 3.8h2l1.5 1.4V8.7h-5z"/></svg>
        <span>555-204-7731</span>
      </li>
      <li>
        <svg viewBox="0 0 10 10" aria-hidden="true"><path d="M.5 2h9v.6L5 5.6.5 2.6zM.5 3.6 5 6.6l4.5-3V8h-9z"/></svg>
        <span>hello@kestrelpower.com</span>
      </li>
    </ul>
    <address class="address">4870, Harbor Line Road<br>Westfield Bay, 204718</address>
  </section>

  <section class="card card-back" aria-label="Business card back">
    <p class="brand-name">KESTREL POWER</p>
  </section>
</main>
</body>
</html>
```